Small Business Consulting Firm Needs Business Card Design

Need a sleek modern business card with 2 sides matching the colors of our logo. We will be placing these with a mailer we are sending out. These business cards will only ever be given to business owners. We operate helping businesses who are struggling with cash flow or finances. If the green and blue design needs to be moved to the right of "Harborline Crest Consulting" for aesthetic purposes that is ok. We will need an editable file if possible. We would like to include the reps name, email, website, and phone number. For now just use Peter Vance, pvance@harborlinecrest.com, www.harborlinecrest.com, and 833-555-0172.

```html
<!DOCTYPE html>
<html lang="en">
<head>
<meta charset="UTF-8">
<title>Harborline Crest Consulting — Business Card</title>
<link rel="stylesheet" href="https://fonts.googleapis.com/css2?family=Montserrat:wght@400;500;600&display=swap">
<style>
  :root {
    --stage: #2f2f31;
    --navy-deep: #0a2f57;
    --navy-light: #1f6b9f;
    --brand-blue: #0f5c99;
    --brand-green: #6cb33f;
    --ink: #3a3a3a;
    --paper: #ffffff;
    --on-navy: #f2f6fa;
  }
  * { box-sizing: border-box; margin: 0; padding: 0; }
  html, body { width: 1200px; height: 900px; overflow: hidden; }
  body {
    background: var(--stage);
    font-family: "Montserrat", Arial, sans-serif;
    position: relative;
  }
  .card {
    position: absolute;
    width: 700px;
    height: 400px;
    box-shadow: 0 10px 30px rgba(0,0,0,.45);
    overflow: hidden;
  }

  /* Front */
  .card-front {
    left: 330px; top: 40px;
    background: linear-gradient(120deg, var(--navy-deep) 0%, #134a7c 55%, var(--navy-light) 100%);
    color: var(--on-navy);
    text-align: center;
  }
  .front-brand {
    position: absolute;
    left: 0; right: 0; top: 110px;
    display: flex; flex-direction: column; align-items: center;
  }
  .brand-square {
    width: 58px; height: 58px;
    background: var(--brand-green);
    margin-bottom: 22px;
  }
  .brand-name {
    font-weight: 500;
    font-size: 30px;
    letter-spacing: 2px;
    text-transform: uppercase;
    line-height: 1;
  }
  .brand-sub {
    font-weight: 500;
    font-size: 14px;
    letter-spacing: 6px;
    text-transform: uppercase;
    margin-top: 6px;
  }
  .front-web {
    position: absolute;
    left: 0; right: 0; bottom: 44px;
    font-size: 15px;
    letter-spacing: 3.5px;
    text-transform: uppercase;
  }

  /* Back */
  .card-back {
    left: 170px; top: 470px;
    background: var(--paper);
    color: var(--ink);
  }
  .back-brand {
    position: absolute;
    left: 48px; top: 40px;
    display: flex; align-items: center; gap: 16px;
  }
  .back-brand .brand-square { width: 54px; height: 54px; margin: 0; }
  .back-brand .brand-name { font-size: 26px; color: var(--ink); }
  .back-brand .brand-sub { font-size: 12px; color: var(--ink); letter-spacing: 5px; text-align: center; }
  .divider {
    position: absolute;
    left: 48px; right: 48px; top: 218px;
    height: 2px;
    background: var(--brand-blue);
  }
  .contact-list {
    position: absolute;
    left: 48px; top: 244px;
    list-style: none;
  }
  .contact-item {
    display: flex; align-items: center; gap: 12px;
    font-size: 19px;
    height: 30px;
  }
  .contact-item svg { width: 20px; height: 20px; fill: var(--brand-blue); flex: none; }
  .rep {
    position: absolute;
    right: 48px; top: 246px;
    text-align: right;
  }
  .rep-name {
    color: var(--brand-blue);
    font-weight: 600;
    font-size: 23px;
    letter-spacing: 1.5px;
    text-transform: uppercase;
  }
  .rep-title { font-size: 16px; margin-top: 4px; }
  .bottom-band {
    position: absolute;
    left: 0; right: 0; bottom: 0;
    height: 30px;
    background: var(--brand-blue);
  }
</style>
</head>
<body>

<section class="card card-front">
  <div class="front-brand">
    <div class="brand-square"></div>
    <div class="brand-name">Harborline Crest</div>
    <div class="brand-sub">Consulting</div>
  </div>
  <div class="front-web">www.harborlinecrest.com</div>
</section>

<section class="card card-back">
  <div class="back-brand">
    <div class="brand-square"></div>
    <div>
      <div class="brand-name">Harborline Crest</div>
      <div class="brand-sub">Consulting</div>
    </div>
  </div>

  <div class="divider"></div>

  <ul class="contact-list">
    <li class="contact-item">
      <svg viewBox="0 0 24 24" aria-hidden="true"><path d="M6.6 10.8a15.1 15.1 0 0 0 6.6 6.6l2.2-2.2c.3-.3.7-.4 1-.2 1.1.4 2.3.6 3.6.6.6 0 1 .4 1 1V20c0 .6-.4 1-1 1A17 17 0 0 1 3 4c0-.6.4-1 1-1h3.5c.6 0 1 .4 1 1 0 1.3.2 2.5.6 3.6.1.3 0 .7-.2 1z"/></svg>
      <span>833 555 0172</span>
    </li>
    <li class="contact-item">
      <svg viewBox="0 0 24 24" aria-hidden="true"><path d="M2 5h20v14H2z M3 6l9 7 9-7" stroke="#fff" stroke-width="1.6"/></svg>
      <span>pvance@harborlinecrest.com</span>
    </li>
    <li class="contact-item">
      <svg viewBox="0 0 24 24" aria-hidden="true"><circle cx="12" cy="12" r="10"/><path d="M2 12h20M12 2c3 3 3 17 0 20M12 2c-3 3-3 17 0 20" stroke="#fff" stroke-width="1.3" fill="none"/></svg>
      <span>www.harborlinecrest.com</span>
    </li>
  </ul>

  <div class="rep">
    <div class="rep-name">Peter Vance</div>
    <div class="rep-title">CEO | Founder</div>
  </div>

  <div class="bottom-band"></div>
</section>

</body>
</html>
```